Touring Cabaret Seasons Needs a Poster Design

We need a poster design for upcoming Cabaret seasons in Melbourne and Adelaide (Australia) for a prestigious festival.

Show is titled "Here's a Small Thing I Dreamed Up Last Week..." and is a comedy parody of bad cabaret and deluded performers. We'd like the poster to reflect the comedy of the piece without being silly and inaccessable.

Artist has recently won awards for this show and these will need to be listed as a part of the design.

I have attached a couple of photographs that can be used - one is the artist with a blank book cover and these could be used to overlay text.

Would like it to not look too wordy, however I realise we've asked for a lot of text to be included.

Target Market(s)

Ages 20 - 40 cabaret or comedy fans.

Industry/Entity Type

Festival

Requirements
Must have
• TEXT:
The Velvet Parlour presents:
Here's a Small Thing I Dreamed Up Last Week...

TEXT:
WINNER of BEST CABARET, BEST WRITING and PEOPLE’S CHOICE awards at Quick + Tidy Revue 2011

TEXT:
The Lantern Room (Melbourne)
Feb 23rd to the 26th

Le Corbeau, REVedge(Adelaide)
March 3rd and 4th

QUOTES:
“...the funniest things in spandex. 4.5 stars” – The Courier Post on Rally! A revue about lawn bowls.

“a clever dissection of bad cabaret” – Owen Blackwood, The Courier Post on Quick + Tidy Revue
Nice to have
• TEXT:
The last time someone showed you a little something they were working on, did you lose an hour of your life you will never get back? Don’t worry – we’ve all been there.

TEXT:
Composer and co-writer of Rally! (A revue about lawn bowls) and WINNER of BEST CABARET, BEST WRITING and PEOPLE’S CHOICE awards at Quick + Tidy Revue 2011, presents her full show, with more original music and helpful anecdotes.

WEBSITE:
More info at www.mingleface.example/thevelvetparlour

```html
<!DOCTYPE html>
<html lang="en">
<head>
<meta charset="utf-8">
<title>The Velvet Parlour – Here's a Small Thing I Dreamed Up Last Week...</title>
<link rel="stylesheet" href="https://fonts.googleapis.com/css2?family=Architects+Daughter&family=Tinos&display=swap">
<style>
  :root {
    --sky: #b8e4ea;
    --cover: #f6f4ec;
    --title-blue: #a8d8e0;
    --ink-white: #ffffff;
    --photo-light: #d9d3cb;
    --photo-dark: #98a0ab;
  }
  html, body {
    margin: 0;
    padding: 0;
    overflow: hidden;
  }
  .poster {
    position: relative;
    width: 848px;
    height: 1200px;
    background: var(--sky);
    overflow: hidden;
    font-family: "Tinos", "Times New Roman", serif;
    color: var(--ink-white);
  }
  .photo-area {
    position: absolute;
    left: 0;
    top: 0;
  }
  .cover-title {
    position: absolute;
    left: 126px;
    top: 596px;
    width: 340px;
    font-family: "Architects Daughter", cursive;
    color: var(--title-blue);
    text-transform: uppercase;
  }
  .cover-title .presenter {
    margin: 0 0 22px;
    font-size: 16px;
    letter-spacing: 0.3px;
  }
  .cover-title .show-name {
    margin: 0;
    font-size: 36px;
    font-weight: 400;
    line-height: 75px;
  }
  .details {
    position: absolute;
    left: 503px;
    top: 597px;
    width: 310px;
    font-size: 12.5px;
    line-height: 16px;
  }
  .details p { margin: 0 0 18px; }
  .venue .dates { display: block; padding-left: 18px; }
  .venue-adelaide { padding-left: 18px; }
  .venue-adelaide .dates { padding-left: 0; }
  .quote {
    position: absolute;
    margin: 0;
  }
  .quote .line {
    font-size: 19px;
    line-height: 24px;
  }
  .quote .source {
    font-size: 12.5px;
    line-height: 15px;
  }
  .quote-rally { left: 497px; top: 762px; width: 345px; }
  .quote-rally .source-cont { display: block; padding-left: 50px; }
  .quote-revue { left: 575px; top: 852px; width: 270px; }
  .quote-revue .line-2 { padding-left: 6px; }
  .quote-revue .source-cont { display: block; padding-left: 6px; }
  .bio {
    position: absolute;
    left: 593px;
    top: 972px;
    width: 232px;
    font-size: 12.5px;
    line-height: 15.5px;
  }
  .bio p { margin: 0 0 17px; }
</style>
</head>
<body>
<main class="poster">
  <svg class="photo-area" width="848" height="1200" viewBox="0 0 848 1200" role="img" aria-label="Photograph of the performer peering over an open blank book held up in front of her">
    <defs>
      <linearGradient id="photoTone" x1="0" y1="0" x2="0" y2="1">
        <stop offset="0" stop-color="var(--photo-light)"/>
        <stop offset="1" stop-color="var(--photo-dark)"/>
      </linearGradient>
    </defs>
    <rect x="0" y="30" width="492" height="1170" fill="url(#photoTone)"/>
    <rect x="0" y="500" width="492" height="650" fill="var(--cover)"/>
  </svg>

  <header class="cover-title">
    <p class="presenter">The Velvet Parlour presents:</p>
    <h1 class="show-name">Here's a small<br>thing I<br>dreamed up<br>last week...</h1>
  </header>

  <section class="details">
    <p class="awards">WINNER of BEST CABARET, BEST WRITING and PEOPLE’S CHOICE awards at Quick + Tidy Revue 2011</p>
    <p class="venue">The Lantern Room (Melbourne)<span class="dates">Feb 23rd to the 26th</span></p>
    <p class="venue venue-adelaide">Le Corbeau, REVedge(Adelaide)<span class="dates">March 3rd and 4th</span></p>
  </section>

  <blockquote class="quote quote-rally">
    <span class="line">“...the funniest things in spandex.<br>4.5 stars”</span>
    <span class="source"> – The Courier Post on Rally!<span class="source-cont">A revue about lawn bowls.</span></span>
  </blockquote>

  <blockquote class="quote quote-revue">
    <span class="line">“a clever dissection of<br><span class="line-2">bad cabaret”</span></span>
    <span class="source"> – Owen Blackwood,<span class="source-cont">The Courier Post on Quick + Tidy Revue</span></span>
  </blockquote>

  <section class="bio">
    <p>Composer and co-writer of Rally! (A revue about lawn bowls) and WINNER of BEST CABARET, BEST WRITING and PEOPLE’S CHOICE awards at Quick + Tidy Revue 2011, presents her full show, with more original music and helpful anecdotes.</p>
    <p>More info at<br>www.mingleface.example/<br>thevelvetparlour</p>
  </section>
</main>
</body>
</html>
```